Business Cards and Stationary for Education Business with focus on social media
KiteHollow Education
Bright & Fun-filled
Mirela Dowsett
Managing Director
TBA 6/12
mirela.dowsett@kitehollowlearning.example
www.kitehollowlearning.example
KiteHollow Education runs seminars for parents and children to attend together aimed at online safety in the area of social media.
MirelaD MirelaD
Hi Designers, I have also decided to go with the logos rather than letter representations of Phone, E-mail etc. Could you please change these in the submissions you have left? Thank you Mirela
Hi Designers, Can whomever sees this first please replicate the #120 design for the front of a card in blue. I have written Pruv 3 messages and he hasn't replied so I am unsure if he is still active on this site. Warm Regards Mirela
Hi Designers, As mentioned in my initial comment I don't like green to dominate my cards. Also please submit a different front and back for each design. Warm Regards Mirela
Hi Designers, Thank you for your great submissions so far. Can I ask that you please submit back and front of business card each time. If it is 1 sided I will eliminate it as I would prefer to have the sides differ. I like use of blue and orange in block colour over green so please take this into consideration. I will give you all some individual feedback asap. Warm Regards Mirela

```html
<!DOCTYPE html>
<html lang="en">
<head>
<meta charset="utf-8">
<title>KiteHollow Education – Business Card</title>
<link href="https://fonts.googleapis.com/css2?family=Arimo:wght@400;700&display=swap" rel="stylesheet">
<style>
  :root {
    --backdrop: #e9e9e7;
    --card-white: #ffffff;
    --brand-blue: #3aaee6;
    --brand-blue-deep: #2a9fd8;
    --brand-orange: #f39a1e;
    --ink: #6d6d6d;
    --ink-light: #9a9a9a;
    --on-blue: #ffffff;
  }
  * { box-sizing: border-box; margin: 0; padding: 0; }
  html, body {
    width: 1200px; height: 600px; overflow: hidden;
    background: var(--backdrop);
    font-family: "Arimo", Arial, sans-serif;
  }
  .stage {
    position: relative; width: 1200px; height: 600px;
  }
  .card {
    position: absolute; top: 150px;
    width: 520px; height: 300px;
    border-radius: 14px;
    box-shadow: 0 6px 18px rgba(0,0,0,0.18);
    overflow: hidden;
  }
  /* Front */
  .card-front { left: 50px; background: var(--card-white); }
  .brand {
    position: absolute; top: 58px; right: 40px;
    display: flex; align-items: center; gap: 10px;
  }
  .brand-square {
    width: 34px; height: 34px;
    background: var(--brand-blue);
  }
  .brand-name {
    font-weight: 700; font-size: 22px; line-height: 1;
    color: var(--brand-blue);
    width: 120px;
  }
  .ref-code {
    position: absolute; top: 142px; right: 40px;
    font-size: 10px; color: var(--ink);
  }
  .holder { position: absolute; left: 28px; top: 170px; }
  .holder-name {
    font-size: 15px; color: var(--brand-orange);
  }
  .holder-role {
    font-size: 8px; color: var(--brand-blue); margin-top: 3px;
  }
  .accent-orange {
    position: absolute; left: 28px; top: 206px;
    width: 120px; height: 5px; background: var(--brand-orange);
    border-radius: 3px;
  }
  .accent-blue {
    position: absolute; left: 148px; top: 207px;
    width: 345px; height: 2px; background: var(--brand-blue);
  }
  .contacts {
    position: absolute; left: 300px; top: 174px;
    list-style: none;
  }
  .contacts li {
    display: flex; align-items: center; gap: 8px;
    font-size: 9px; color: var(--ink);
    height: 16px;
  }
  .contacts li:nth-child(2) { margin-top: 22px; }
  .contacts svg { width: 10px; height: 10px; flex: none; }
  .contacts .icon { stroke: var(--brand-orange); fill: none; stroke-width: 1.4; }
  /* Back */
  .card-back {
    left: 630px;
    background: linear-gradient(160deg, var(--brand-blue), var(--brand-blue-deep));
  }
  .back-brand {
    position: absolute; top: 100px; left: 0; right: 0;
    display: flex; justify-content: center; align-items: center; gap: 10px;
  }
  .back-brand .brand-square { background: var(--on-blue); }
  .back-brand .brand-name { color: var(--on-blue); }
  .back-web {
    position: absolute; bottom: 60px; left: 0; right: 0;
    text-align: center; font-size: 10px; color: var(--on-blue);
  }
</style>
</head>
<body>
<main class="stage">
  <section class="card card-front" aria-label="Card front">
    <div class="brand">
      <span class="brand-square"></span>
      <span class="brand-name">KiteHollow Education</span>
    </div>
    <p class="ref-code">TBA 6/12</p>
    <div class="holder">
      <p class="holder-name">Mirela Dowsett</p>
      <p class="holder-role">Managing Director</p>
    </div>
    <span class="accent-orange"></span>
    <span class="accent-blue"></span>
    <ul class="contacts">
      <li>
        <svg viewBox="0 0 10 10"><path class="icon" d="M2 1h2l1 2.5-1.3 1a5 5 0 0 0 2 2l1-1.3L9 6.5v2a1 1 0 0 1-1 1A8 8 0 0 1 .5 2a1 1 0 0 1 1-1z"/></svg>
        (07) 5550 0142
      </li>
      <li>
        <svg viewBox="0 0 10 10"><rect class="icon" x="0.7" y="2" width="8.6" height="6"/><path class="icon" d="M.7 2L5 5.5 9.3 2"/></svg>
        mirela.dowsett@kitehollowlearning.example
      </li>
      <li>
        <svg viewBox="0 0 10 10"><circle class="icon" cx="5" cy="5" r="4.2"/><path class="icon" d="M.8 5h8.4M5 .8c-2.4 2.6-2.4 5.8 0 8.4M5 .8c2.4 2.6 2.4 5.8 0 8.4"/></svg>
        www.kitehollowlearning.example
      </li>
    </ul>
  </section>

  <section class="card card-back" aria-label="Card back">
    <div class="back-brand">
      <span class="brand-square"></span>
      <span class="brand-name">KiteHollow Education</span>
    </div>
    <p class="back-web">www.kitehollowlearning.example</p>
  </section>
</main>
</body>
</html>
```